Sprouts at Desk

We need a logo and graphich design for a one page text for our Sprouts @desk program, it would nened to match or be inspired from our corporate indentity which can be seen at www.tolvaro-partners.com

Dear XXX
BRX is proud to launch its first ever SPROUTS @ DESK day! We invite you and your child(ren) to join us on this special day, and strengthen the connection between education and work, and your relationship between parent and child(ren).

Who? All children, all ages
Where? BRX offices
When? January 29th, from 13h – 17h

Sprouts @ Desk is the perfect time to start shaping your children’s future through education and experience at BRX with a program tailored to target each age group. There will be group activities and sessions, as well as one on one time for parents and their children.
We are excited to work together with you and your children to create a true sense of community, and celebrate the opportunities and possibilities for the next generation. It’s a day to share your passion and know-how and show what happens when you are at work. We will show children the value of education and help them discover the power and potential of a balanced work and family life. We would like to give you and your children an opportunity to express their future goals and dreams and help begin together the steps towards achieving these through the follow up with Sprouts @ Hope. BRX is developing a multi-program to enable parents and children to realize the future they dream of.
We look forward to seeing you @ Work!

```html
<!DOCTYPE html>
<html lang="en">
<head>
<meta charset="utf-8">
<title>Sprouts @ Desk Day – Invitation</title>
<link rel="stylesheet" href="https://fonts.googleapis.com/css2?family=Roboto:wght@300;400;700&display=swap">
<style>
  :root {
    --brand-pink: #ec0a6e;
    --paper: #ffffff;
    --ink-grey: #7a7a7a;
    --body-ink: #3a3a3a;
    --rule-pink: #f27bb0;
    --photo-dark: #4a4a4a;
    --photo-light: #b9b9b9;
  }
  * { margin: 0; padding: 0; box-sizing: border-box; }
  html, body { width: 1200px; height: 900px; overflow: hidden; }
  body {
    background: var(--brand-pink);
    font-family: "Roboto", Arial, sans-serif;
    position: relative;
  }
  .invitation {
    position: absolute;
    left: 35px; top: 35px;
    width: 1130px; height: 830px;
    background: var(--paper);
    border-radius: 46px;
  }
  .event-mark {
    position: absolute;
    left: 59px; top: 82px;
    width: 355px; height: 287px;
    display: flex; align-items: center; justify-content: center; gap: 14px;
  }
  .event-mark__square {
    width: 34px; height: 34px;
    background: var(--brand-pink);
    flex: none;
  }
  .event-mark__name {
    color: var(--brand-pink);
    font-weight: 700;
    font-size: 34px;
    line-height: 1.1;
    text-transform: uppercase;
  }
  .letter {
    position: absolute;
    left: 468px; top: 86px;
    width: 585px;
    color: var(--ink-grey);
    font-weight: 300;
    font-size: 19px;
    line-height: 28.5px;
  }
  .event-facts {
    position: absolute;
    left: 468px; top: 243px;
    color: var(--ink-grey);
    font-weight: 700;
    font-size: 30px;
    line-height: 38px;
    list-style: none;
  }
  .divider {
    position: absolute;
    left: 59px; top: 428px;
    width: 996px; height: 1px;
    background: var(--rule-pink);
  }
  .body-column {
    position: absolute;
    top: 484px;
    width: 315px;
    color: var(--body-ink);
    font-weight: 300;
    font-size: 14.6px;
    line-height: 21.2px;
  }
  .body-column p + p { margin-top: 21.2px; }
  .body-column--first { left: 53px; }
  .body-column--second { left: 394px; }
  .photo-children {
    position: absolute;
    left: 737px; top: 486px;
    width: 317px; height: 267px;
    background: linear-gradient(180deg, var(--photo-light) 0%, #8e8e8e 45%, var(--photo-dark) 100%);
  }
</style>
</head>
<body>
  <main class="invitation">
    <div class="event-mark">
      <span class="event-mark__square"></span>
      <span class="event-mark__name">Sprouts @ Desk Day!</span>
    </div>

    <p class="letter">Dear XXX<br>BRX is proud to launch its first ever SPROUTS @ DESK day! We invite you and your child(ren) to join us on this special day, and strengthen the connection between education and work, and your relationship between parent and child(ren).</p>

    <ul class="event-facts">
      <li>Who? All children, all ages</li>
      <li>Where? BRX offices</li>
      <li>When? January 29th, from 13h – 17h</li>
    </ul>

    <div class="divider"></div>

    <div class="body-column body-column--first">
      <p>Sprouts @ Desk is the perfect time to start shaping your children’s future through education and experience at BRX with a program tailored to target each age group. There will be group activities and sessions, as well as one on one time for parents and their children.</p>
      <p>We are excited to work together with you and your children to create a true sense of community, and celebrate the opportunities and possibilities for the next generation. It’s a day to share your passion and know-how</p>
    </div>

    <div class="body-column body-column--second">
      <p>and show what happens when you are at work. We will show children the value of education and help them discover the power and potential of a balanced work and family life. We would like to give you and your children an opportunity to express their future goals and dreams and help begin together the steps towards achieving these through the follow up with Sprouts @ Hope. BRX is developing a multi-program to enable parents and children to realize the future they dream of.<br>We look forward to seeing you @ Work!</p>
    </div>

    <div class="photo-children" role="img" aria-label="Black and white photo of two young children running across a grassy field"></div>
  </main>
</body>
</html>
```